Harbor Petroleum Business Cards

I would like to design some options for about 10 sets of double sided business cards for our team with a raised logo with a Silver glossy finished logo. We are a privately funded upstream Oil & Gas producer drilling vertical wells in Central Oklahoma with a long term production (ROI driven) strategy that we implement through an annual drilling program. We are focused on a shallow / vertical / long life / low decline strategy. We are based in downtown Tulsa Oklahoma. I have attached a sample business card and a picture of our hallway logo which we would like to replicate on the business cards.

Target Market(s)

SEC Accredited Investors and other Oil & Gas Operators

Industry/Entity Type

Upstream Oil & Gas

Contact Information for Business Card

You can see the sample photo attached, but email / website / address / direct phone / Cell Phone / Name / Title / Fax

Font styles to use
Other font styles liked:
• Felix Titling

Colors
0054AA
0677BA
7BADD7
CADEEF
E8F1F8

Requirements
Must have
• Glossy raised logo
Nice to have
• Possibly a new logo.
Should not have
• No Greens /

```html
<!DOCTYPE html>
<html lang="en">
<head>
<meta charset="utf-8">
<title>Harbor Petroleum Business Cards</title>
<link rel="stylesheet" href="https://fonts.googleapis.com/css2?family=Cinzel:wght@500&family=Poppins:wght@400;600&display=swap">
<style>
  :root {
    --blue-deep: #0054AA;
    --blue-mid: #0677BA;
    --blue-band: #0f52ab;
    --ink: #3a3a3a;
    --paper: #ffffff;
    --silver: #dcdfe3;
    --stage: #2a2a2a;
  }
  * { margin: 0; padding: 0; box-sizing: border-box; }
  html, body { width: 1093px; height: 1200px; overflow: hidden; }
  body { background: var(--stage); position: relative; font-family: "Poppins", sans-serif; }

  .card { position: absolute; left: 265px; width: 578px; height: 356px; border-radius: 24px; overflow: hidden; }
  .card-front { top: 226px; background: var(--paper); }
  .card-back { top: 621px; background: linear-gradient(30deg, var(--blue-deep) 0%, var(--blue-mid) 100%); }

  .brand-name { font-family: "Cinzel", serif; font-weight: 500; white-space: nowrap; text-align: center; }
  .card-front .brand-name { position: absolute; left: 20px; width: 270px; top: 200px; font-size: 17px; color: var(--blue-deep); }
  .card-back .brand-name { position: absolute; left: 0; width: 100%; top: 210px; font-size: 30px; color: var(--silver); letter-spacing: 0.5px; }

  .divider { position: absolute; left: 297px; top: 71px; width: 1.5px; height: 210px; background: var(--blue-deep); }

  .contact { position: absolute; left: 317px; top: 70px; color: var(--ink); }
  .person-name { font-weight: 600; font-size: 18px; color: var(--blue-deep); line-height: 22px; white-space: nowrap; }
  .person-name .credential { font-weight: 400; font-size: 15px; }
  .person-title { font-size: 16.5px; line-height: 20px; }

  .contact-list { list-style: none; margin-top: 15px; }
  .contact-list li { display: flex; align-items: center; font-size: 17px; line-height: 21px; white-space: nowrap; }
  .contact-list svg { width: 15px; height: 15px; margin-right: 6px; fill: var(--blue-deep); flex: none; }
  .web-domain { color: var(--blue-deep); }

  .address { margin-top: 12px; margin-left: 2px; font-size: 17px; line-height: 21px; }

  .rule-thin { position: absolute; left: 0; right: 0; top: 329px; height: 5px; background: var(--blue-mid); }
  .rule-band { position: absolute; left: 0; right: 0; top: 337px; height: 19px; background: var(--blue-band); }
</style>
</head>
<body>
  <section class="card card-front">
    <div class="brand-name">HARBOR PETROLEUM, LLC</div>
    <div class="divider"></div>
    <div class="contact">
      <p class="person-name">DALTON R. WHITFIELD, <span class="credential">CPL</span></p>
      <p class="person-title">Executive Vice President</p>
      <ul class="contact-list">
        <li><svg viewBox="0 0 16 16" aria-hidden="true"><path d="M3.5 1.5l2.5 3-1.5 1.5c.8 2 2.5 3.7 4.5 4.5L10.5 9l3 2.5-1.5 2.5C7 14 2 9 1.5 3z"/></svg>044-123 456 789</li>
        <li><svg viewBox="0 0 16 16" aria-hidden="true"><path d="M4 1h8v14H4zM5.3 2.3v9.4h5.4V2.3zM7.3 12.6h1.4v1.2H7.3z" fill-rule="evenodd"/></svg>044-123 456 789</li>
        <li><svg viewBox="0 0 16 16" aria-hidden="true"><path d="M4 1h8v4H4zM1 6h14v6h-2.5v3h-9v-3H1zM5 10v4h6v-4z" fill-rule="evenodd"/></svg>044-123 456 789</li>
        <li><svg viewBox="0 0 16 16" aria-hidden="true"><path d="M1 3h14v10H1zM2 4.2l6 4.6 6-4.6v-.1H2z" fill-rule="evenodd"/></svg>info@webname.com</li>
        <li><svg viewBox="0 0 16 16" aria-hidden="true"><path d="M8 1a7 7 0 110 14A7 7 0 018 1zm0 1.3v11.4M2.3 8h11.4M3 5h10M3 11h10M8 1.5c-3 3.5-3 9.5 0 13M8 1.5c3 3.5 3 9.5 0 13" fill="none" stroke="#0054AA" stroke-width="1.1"/></svg>www.<span class="web-domain">websitename</span>.com</li>
      </ul>
      <p class="address">421, Address line here<br>45452,Country Name</p>
    </div>
    <div class="rule-thin"></div>
    <div class="rule-band"></div>
  </section>

  <section class="card card-back">
    <div class="brand-name">HARBOR PETROLEUM, LLC</div>
  </section>
</body>
</html>
```